Snack Menu for the bowling lanes side of our business.

Build a snack menu from the appetizer and pizza portion of the menu. Some of the sandwiches could be added into this menu.
Industry/Entity Type
Business
Requirements
Must have
- Menu should be bowling themed - using bowling graphics and look different than the restaurant menu.
Nice to have
- The Copperfield Restaurant logo used on menu.

```html
<!DOCTYPE html>
<html lang="en">
<head>
<meta charset="utf-8">
<title>Snack Menu – The Copperfield Restaurant</title>
<link rel="stylesheet" href="https://fonts.googleapis.com/css2?family=Arimo:wght@400;700&family=Arvo:wght@700&family=Bungee&family=Cinzel:wght@700&family=Russo+One&display=swap">
<style>
:root{
  --sky-top:#1a7fd6;
  --sky-mid:#4fb3f0;
  --sky-light:#bfe6fb;
  --ink:#111111;
  --white:#ffffff;
  --red:#d81e1e;
  --panel-grey:#eeeeee;
  --panel-yellow:#f3ec9a;
  --panel-lavender:#e3e3f6;
  --panel-pink:#f5c3c0;
  --pins:#c9161b;
  --pin-white:#eeeeee;
  --ball:#1d1d1f;
}
*{margin:0;padding:0;box-sizing:border-box}
html,body{width:927px;height:1200px;overflow:hidden}
body{font-family:"Arimo",Arial,sans-serif;color:var(--ink)}
.menu{
  position:relative;width:927px;height:1200px;overflow:hidden;
  background:
    linear-gradient(125deg,transparent 38%,rgba(255,255,255,.35) 44%,transparent 50%),
    linear-gradient(150deg,transparent 55%,rgba(255,255,255,.25) 60%,transparent 66%),
    radial-gradient(ellipse at 60% 55%,var(--sky-light) 0%,var(--sky-mid) 45%,var(--sky-top) 100%);
}
.art{position:absolute}
.art--pizza{left:662px;top:0;width:262px;height:190px;border-radius:50% 50% 45% 45%;background:radial-gradient(circle at 50% 45%,#e8b35a,#c8752c 70%,#a85a22)}
.art--pins{left:160px;top:120px;width:150px;height:130px;border-radius:40% 40% 30% 30%;background:radial-gradient(circle at 50% 70%,#e13a30,var(--pins) 70%)}
.art--pin-logo{left:30px;top:760px;width:260px;height:440px;border-radius:45% 45% 20% 20% / 30% 30% 10% 10%;background:linear-gradient(90deg,#cfcfcf,var(--pin-white) 45%,#d6d6d6)}
.art--ball{left:712px;top:1008px;width:197px;height:190px;border-radius:50%;background:radial-gradient(circle at 40% 35%,#555,var(--ball) 60%)}
.brand-name{position:absolute;left:60px;top:960px;width:200px;text-align:center;font-family:"Arimo",Arial,sans-serif;font-weight:700;font-size:26px;line-height:1.2;color:var(--ink)}

.title{position:absolute;font-family:"Bungee",sans-serif;color:var(--white);-webkit-text-stroke:2px var(--red);transform:rotate(-6deg)}
.title--snack{left:40px;top:74px;font-size:74px;letter-spacing:2px}
.title--menu{left:112px;top:222px;font-size:40px;transform:rotate(0)}

.headline{position:absolute;font-family:"Russo One",sans-serif;color:var(--ink);text-shadow:0 0 3px var(--white),0 0 6px var(--white);white-space:nowrap;z-index:2}
.headline--pizza{left:400px;top:132px;font-size:38px;letter-spacing:5px}
.headline--finest{left:462px;top:170px;font-size:30px;letter-spacing:3px}
.headline--specials{left:16px;top:340px;font-size:38px}

.panel{position:absolute;border:5px solid var(--white);border-radius:12px;box-shadow:4px 6px 10px rgba(0,0,0,.35);text-align:center}
.panel--pizza{left:380px;top:200px;width:530px;height:172px;background:var(--panel-grey);padding:14px 4px 0}
.panel--specials{left:46px;top:330px;width:400px;height:444px;background:var(--panel-yellow);padding:62px 6px 0}
.panel--appetizers{left:494px;top:392px;width:424px;height:350px;background:var(--panel-lavender);padding:4px 8px 0}
.panel--more{left:392px;top:706px;width:434px;height:302px;background:var(--panel-pink);padding:6px 10px 0}

.price-line{font-size:17px;font-weight:700;line-height:1.2}
.price-line .cap{font-family:"Cinzel",serif;font-size:24px}
.item-list{font-size:17px;line-height:1.35;margin-top:4px}
.item-list b{font-family:"Arvo",serif}

.section-title{font-family:"Arvo",serif;font-size:40px;line-height:1.05}
.dish{margin-bottom:6px}
.dish__name{font-family:"Arvo",serif;font-weight:700;font-size:23px;line-height:1.1}
.dish__desc{font-size:16.5px;line-height:1.3}
.panel--specials .dish__desc{font-size:16px}
.dish__sizes{font-size:16px;line-height:1.4}
.dish--inline .dish__name{display:inline}
.dish__name--small{font-size:19px}

.sampler{position:absolute;left:236px;top:1036px;width:470px;text-align:center;z-index:3}
.sampler .dish__name{font-size:25px}
.sampler .dish__desc{font-size:17px}
</style>
</head>
<body>
<main class="menu">
  <div class="art art--pizza" role="img" aria-label="Pepperoni pan pizza with a slice cut out"></div>
  <div class="art art--pins" role="img" aria-label="Red bowling pins scattered by a red bowling ball"></div>

  <h1 class="title title--snack">SNACK</h1>
  <div class="title title--menu">MENU</div>

  <section class="panel panel--pizza">
    <p class="price-line"><span class="cap">CHEESE</span> Small 7.25 &nbsp;Medium 9.25 Large 11.25</p>
    <p class="price-line"><span class="cap">ADDITIONAL ITEMS</span> Sm. 1.25 &nbsp;Med. 1.50 Lg. 1.75</p>
    <p class="item-list"><b>Items:</b> Ham. Pepperoni. Hamburger. Italian Sausage. Bacon. Green olives. Black Olives. Onions. Green Peppers Mushrooms. Pepper Rings or Tomatoes.</p>
  </section>

  <h2 class="headline headline--pizza">Homemade Pan Pizza</h2>
  <div class="headline headline--finest">Harbor Falls's Finest</div>

  <section class="panel panel--specials">
    <div class="dish dish--inline">
      <span class="dish__name">Copperfield Special</span>
      <span class="dish__desc">Cheese. Ham Pepperoni. Onions. Green Peppers. Mushrooms and Italian Sausage</span>
      <p class="dish__sizes">Sm. 10.75 &nbsp;Med. 13.75 &nbsp;Lg. 16.50</p>
    </div>
    <div class="dish dish--inline">
      <span class="dish__name">Meat Lovers</span>
      <span class="dish__desc">Cheese. Ham. Pepperoni. Italian Sausage. Bacon and Beef</span>
      <p class="dish__sizes">Sm. 10.75 &nbsp;Med. 13.75 &nbsp;Lg. 16.50</p>
    </div>
    <div class="dish dish--inline">
      <span class="dish__name">Hawaiian Pizza</span>
      <span class="dish__desc">With Pineapple and Ham</span>
      <p class="dish__sizes">Sm. 8.75 Med. 11.25 Lg. 13.75</p>
    </div>
    <div class="dish dish--inline">
      <span class="dish__name">Vegetarian Pizza</span>
      <span class="dish__desc">Mushrooms. Onion. Tomato and Green Peppers</span>
      <p class="dish__sizes">Sm. 8.75 Med. 11.25 Lg. 13.75</p>
    </div>
    <div class="dish">
      <p class="dish__name dish__name--small">Personal 7” Pan Pizza</p>
      <p class="dish__desc">With any 3 items 4.25</p>
    </div>
  </section>
  <h2 class="headline headline--specials">Copperfield Specials</h2>

  <section class="panel panel--appetizers">
    <h2 class="section-title">Appetizers</h2>
    <div class="dish">
      <p class="dish__name">Cheese Bread Squares</p>
      <p class="dish__desc">Copperfield original, our homemade pizza dough loaded with mozzarella cheese with a dusting of parmasan and garlic 4.99</p>
    </div>
    <div class="dish">
      <p class="dish__name">Battered Mushrooms</p>
      <p class="dish__desc">Whole mushrooms battered and fried golden served with dipping sauce 3.99</p>
    </div>
    <div class="dish">
      <p class="dish__name">Battered Cauliflower</p>
      <p class="dish__desc">Cauliflower florets battered and fried golden served with dipping sauce 3.99</p>
    </div>
  </section>

  <section class="panel panel--more">
    <div class="dish">
      <p class="dish__name">Cheddar Cheese Nuggets</p>
      <p class="dish__desc">Wisconsin cheddar cheese breaded and fried golden 3.99</p>
    </div>
    <div class="dish">
      <p class="dish__name">Chicken Tenders</p>
      <p class="dish__desc">Tender and crispy served with your choice of dipping sauce 4.99</p>
    </div>
    <div class="dish">
      <p class="dish__name">Mozzarella Sticks</p>
      <p class="dish__desc">Mozzarella cheese lightly breaded and fried served with your choice of dipping sauce 3.99</p>
    </div>
  </section>

  <div class="art art--pin-logo" role="img" aria-label="Large white bowling pin carrying the restaurant name"></div>
  <p class="brand-name">The Copperfield Restaurant</p>

  <div class="art art--ball" role="img" aria-label="Black bowling ball"></div>

  <section class="sampler">
    <p class="dish__name">Taproom Sampler</p>
    <p class="dish__desc">Beer battered favorites including chicken tenders, mushrooms, shrimp, onion rings, mozzarella cheese sticks, cream cheese stuffed peppers and Taproom fries 6.99</p>
  </section>
</main>
</body>
</html>
```